High end business card design for custom homebuilding company

Looking for a high end business card design that is unique and elegant. Can use embossing, foil printing, laser die cutting, or any high end printing technique or high end paper. Will upload current design so you can see the logo and what we are using currently, but we want something more unique and elegant. I included our logo to help with design.

Target Market(s)

High end custom home buyers of $1.5 million plus homes. Also real estate developers of high end communities.

Industry/Entity Type

Business

Contact Information for Business Card

Double sided. We want something very elegant and expensive looking. We are looking to incorporate a combination of perhaps linen paper or a high end paper, with foil stamping or embossing/debossing to make the card look unique, but still elegant. We tend to use blacks and golds, but are open to any ideas. Looking for creative and unique design.

Colors

Designer to choose colors to be used in the design.

Requirements
Must have
• High end, elegant look. Can use foil, embossing, or high end papers like linen. We want to make the card unique and interesting, but elegant and expensive looking.
Nice to have
• I am including just some cards I saw that looked interesting for one reason or another. I like a clean elegant design and like both the clean white style, and the blacks. So not sure if we want a black design or white. Would like to see both.

```html
<!DOCTYPE html>
<html lang="en">
<head>
<meta charset="utf-8">
<title>Ridgeline Custom Homes – Business Card</title>
<link rel="stylesheet" href="https://fonts.googleapis.com/css2?family=Marcellus&family=Montserrat:wght@500&display=swap">
<style>
  :root {
    --backdrop: #d9d9d9;
    --card: #2a2a2b;
    --card-light: #323233;
    --ink: #0c0c0c;
    --gold: #c9962b;
    --gold-light: #f0c860;
  }
  * { margin: 0; padding: 0; box-sizing: border-box; }
  html, body { width: 1200px; height: 900px; overflow: hidden; }
  body {
    background: var(--backdrop);
    position: relative;
    font-family: "Montserrat", sans-serif;
  }
  .card {
    position: absolute;
    left: 250px;
    width: 700px;
    height: 400px;
    background: radial-gradient(ellipse at 40% 35%, var(--card-light), var(--card) 70%);
    border-bottom: 5px solid var(--gold);
    box-shadow: 0 6px 18px rgba(0,0,0,0.25);
    color: var(--ink);
  }
  .card--back { top: 35px; }
  .card--front { top: 465px; }

  /* back side: contact details */
  .mark {
    position: absolute;
    border-radius: 50%;
    background: var(--ink);
  }
  .card--back .mark { left: 110px; top: 140px; width: 120px; height: 120px; }
  .divider {
    position: absolute;
    left: 300px; top: 90px;
    width: 3px; height: 220px;
    background: var(--ink);
  }
  .details {
    position: absolute;
    left: 335px; top: 92px;
  }
  .details .company {
    font-family: "Marcellus", serif;
    font-size: 34px;
    letter-spacing: 1px;
    line-height: 1;
  }
  .details .tagline {
    font-family: "Marcellus", serif;
    font-size: 12px;
    letter-spacing: 7px;
    margin-top: 4px;
  }
  .details .person {
    font-family: "Marcellus", serif;
    font-size: 20px;
    letter-spacing: 2px;
    margin-top: 30px;
  }
  .details .role {
    font-size: 11px;
    letter-spacing: 2px;
    margin-top: 4px;
  }
  .details .contact {
    list-style: none;
    margin-top: 20px;
    font-size: 14px;
    letter-spacing: 2px;
    line-height: 1.75;
  }

  /* front side: brand lockup */
  .lockup {
    position: absolute;
    left: 60px; top: 135px;
    display: flex;
    align-items: center;
    gap: 22px;
  }
  .card--front .mark { position: static; width: 100px; height: 100px; flex: none; }
  .lockup .company {
    font-family: "Marcellus", serif;
    font-size: 66px;
    letter-spacing: 2px;
    line-height: 1;
  }
  .lockup .tagline {
    font-family: "Marcellus", serif;
    font-size: 24px;
    letter-spacing: 14px;
    margin-top: 6px;
  }
</style>
</head>
<body>
  <section class="card card--back">
    <div class="mark"></div>
    <div class="divider"></div>
    <div class="details">
      <div class="company">RIDGELINE</div>
      <div class="tagline">CUSTOM HOMES</div>
      <div class="person">ELEANOR WHITFIELD</div>
      <div class="role">OWNER</div>
      <ul class="contact">
        <li>CELL: (555) 014-2280</li>
        <li>EMAIL: INFO@RIDGELINEHOMES.COM</li>
        <li>WEB: WWW.RIDGELINEHOMES.COM</li>
      </ul>
    </div>
  </section>

  <section class="card card--front">
    <div class="lockup">
      <div class="mark"></div>
      <div>
        <div class="company">RIDGELINE</div>
        <div class="tagline">CUSTOM HOMES</div>
      </div>
    </div>
  </section>
</body>
</html>
```